BrightMesa Business Card Contest

We are looking for a modern business card that catches attention and is unique. Attached is the brand guide and logo files. Please note that the back side (not the side with our name and info) with be UV raise printed, so have fun with the design there. We want to include Name, Title, Phone number, email, website.

Contact Information for Business Card

Please see project description

```html
<!DOCTYPE html>
<html lang="en">
<head>
<meta charset="utf-8">
<title>BrightMesa Business Card</title>
<link href="https://fonts.googleapis.com/css2?family=Poppins:wght@300;400;600&display=swap" rel="stylesheet">
<style>
  :root {
    --stage-light: #5c5c5c;
    --stage-dark: #2e2e2e;
    --card: #1d1f25;
    --ink: #ffffff;
    --ink-soft: #d9dbe0;
    --back-mark: #33363f;
    --red: #e3261a;
    --orange: #f07a12;
    --slate: #a9b7c8;
    --sky: #8fb8d8;
    --cyan: #1fb4e8;
    --blue: #2774c4;
    --navy: #1e3f8a;
  }
  * { margin: 0; padding: 0; box-sizing: border-box; }
  html, body { width: 1200px; height: 781px; overflow: hidden; }
  body {
    background: radial-gradient(ellipse at 50% 45%, var(--stage-light), var(--stage-dark) 80%);
    font-family: "Poppins", sans-serif;
    position: relative;
  }
  .card {
    position: absolute;
    top: 242px;
    width: 520px;
    height: 297px;
    background: var(--card);
    border-radius: 4px;
    box-shadow: 0 18px 40px rgba(0,0,0,.45);
    overflow: hidden;
  }
  .card-back { left: 45px; display: flex; align-items: center; justify-content: center; }
  .card-front { left: 635px; }
  .back-name {
    font-size: 46px; font-weight: 600; color: var(--back-mark); letter-spacing: .5px;
  }
  .brand {
    position: absolute; left: 40px; top: 118px;
    display: flex; align-items: center; gap: 10px;
    font-size: 34px; font-weight: 400; color: var(--ink);
  }
  .brand-dot { width: 14px; height: 14px; border-radius: 50%; background: var(--cyan); }
  .divider {
    position: absolute; left: 292px; top: 78px; width: 2px; height: 126px;
    background: linear-gradient(to bottom, var(--red), var(--sky) 50%, var(--navy));
  }
  .person { position: absolute; left: 314px; top: 82px; color: var(--ink); }
  .person-name { font-size: 22px; font-weight: 600; line-height: 1.1; }
  .person-title { font-size: 12px; font-weight: 300; color: var(--ink-soft); margin-bottom: 12px; }
  .contact { list-style: none; font-size: 12px; font-weight: 300; color: var(--ink-soft); }
  .contact li { display: flex; align-items: center; gap: 7px; line-height: 21px; }
  .contact svg { width: 11px; height: 11px; fill: none; stroke: var(--ink); stroke-width: 1.6; }
  .color-strip { position: absolute; left: 0; right: 0; bottom: 0; height: 9px; display: flex; }
  .color-strip span { height: 100%; }
</style>
</head>
<body>
  <section class="card card-back" aria-label="Card back">
    <span class="back-name">BrightMesa</span>
  </section>

  <section class="card card-front" aria-label="Card front">
    <div class="brand"><span class="brand-dot"></span>BrightMesa</div>
    <div class="divider"></div>
    <div class="person">
      <p class="person-name">Dana Reyes</p>
      <p class="person-title">Director</p>
      <ul class="contact">
        <li><svg viewBox="0 0 12 12"><path d="M3 1 L5 3.5 L4 5 Q5.5 7.5 7 8 L8.5 7 L11 9 L9.5 11 Q4 10 1 3 Z"/></svg>555-214-7730</li>
        <li><svg viewBox="0 0 12 12"><rect x="1" y="2.5" width="10" height="7"/><path d="M1 2.5 L6 7 L11 2.5"/></svg>dr@brightmesa.com</li>
        <li><svg viewBox="0 0 12 12"><circle cx="6" cy="6" r="5"/><path d="M1 6 H11 M6 1 Q2.5 6 6 11 Q9.5 6 6 1"/></svg>brightmesa.com</li>
      </ul>
    </div>
    <div class="color-strip">
      <span style="width:14%;background:var(--red)"></span>
      <span style="width:8%;background:var(--orange)"></span>
      <span style="width:12%;background:var(--slate)"></span>
      <span style="width:13%;background:var(--sky)"></span>
      <span style="width:18%;background:var(--cyan)"></span>
      <span style="width:15%;background:var(--blue)"></span>
      <span style="width:20%;background:var(--navy)"></span>
    </div>
  </section>
</body>
</html>
```